Geschäftsunterlagen mit vorhandenem Logo
Zielgruppe
- Immobilienmakler.
- Vermietung und Verkauf von Immobilien
- Eigentümer, Bauträger, Hausverwaltungen, Immobilienentwickler, Wohnungsbaugesellschaften, Käufer und Mieter.
Aufgabenstellung
Wir suchen ein neues Design für unsere Geschäftsunterlagen. Es soll dem Betrachter ein gutes Gefühl vermittelt. Es soll seriös, edel und dynamisch wirken, aber auch vertrauensvoll und kompetent.
Wir suchen neue Designs für folgende Unterlagen, das Logo soll hierbei etwas stärker im Vordergrund stehen :
- Visitenkarten ( Text= Logo, mein Name Jonas Brettler, Handynr. und Webseite )
- Briefpapier ( Text= Logo, Firmenname, Adresse, email, Tel-Nr., event. Bankverbindung ) + Briefumschlag ( Din-Lang ) + email-Vorlage ( Logo + Firmenname, Adresse + Telefon )
- Mappe für Unterlagen ( Din A4 )
- Vermietungsschild und Verkaufsschild fürs Objekt ( 1. H=700mm x B=440mm und 2. H=600 x B 1000mm ) Falls die Schilder zu viel sind, lassen Sie die Entwürfe bitte weg. Priorität haben die anderen Unterlagen.
Logo ist vorhanden, die Schrift kann noch variiert werden.
Falls Sie Fragen haben, schreiben Sie uns bitte an.

```html
<!DOCTYPE html>
<html lang="de">
<head>
<meta charset="utf-8">
<title>Brettler Immobilien – Briefpapier</title>
<link rel="stylesheet" href="https://fonts.googleapis.com/css2?family=Arimo:wght@400;700&display=swap">
<style>
  :root {
    --backdrop: #efefef;
    --paper: #ffffff;
    --navy: #1d2d52;
    --blue: #2f5f9e;
    --sky: #4d8ccc;
    --ink: #111111;
    --logo-ink: #2f2f33;
    --signature-tone: #2c2f8f;
  }
  * { box-sizing: border-box; margin: 0; padding: 0; }
  html, body { width: 1200px; height: 1200px; overflow: hidden; }
  body {
    background: var(--backdrop);
    font-family: "Arimo", Arial, sans-serif;
    position: relative;
  }
  .letterhead {
    position: absolute;
    left: 370px; top: 115px;
    width: 706px; height: 1000px;
    background: var(--paper);
    box-shadow: 6px 8px 14px rgba(0,0,0,0.35);
    overflow: hidden;
  }
  .letterhead-shapes { position: absolute; inset: 0; }
  .brand {
    position: absolute;
    display: flex; align-items: center; gap: 12px;
  }
  .brand-dot {
    width: 54px; height: 54px; border-radius: 50%;
    background: var(--blue);
    flex: none;
  }
  .brand-name {
    color: var(--logo-ink);
    font-weight: 400;
    line-height: 1;
  }
  .brand-name .primary { display: block; font-size: 33px; letter-spacing: 1px; }
  .brand-name .secondary { display: block; font-size: 15px; letter-spacing: 2.6px; margin-top: 3px; }
  .letterhead .brand { left: 85px; top: 98px; }
  .standalone-brand { left: 60px; top: 981px; }

  .subject {
    position: absolute; left: 81px; top: 218px;
    font-size: 13.5px; color: var(--navy);
  }
  .letter-body {
    position: absolute; left: 81px; top: 265px; width: 535px;
    font-size: 12.4px; line-height: 22.5px; color: var(--ink);
  }
  .letter-body p + p { margin-top: 9px; }
  .signature-mark {
    position: absolute; left: 84px; top: 714px;
    width: 168px; height: 78px;
    background: linear-gradient(100deg, rgba(44,47,143,0.18), rgba(44,47,143,0.05));
  }
  .signature-label {
    position: absolute; left: 81px; top: 808px;
    font-size: 15px; color: var(--navy);
  }
  .contact {
    position: absolute; right: 60px; top: 882px;
    list-style: none; color: #ffffff; font-size: 11.5px;
  }
  .contact li {
    display: flex; justify-content: flex-end; align-items: center;
    gap: 14px; height: 24.5px;
  }
  .contact svg { width: 14px; height: 14px; fill: #ffffff; flex: none; }
</style>
</head>
<body>
  <article class="letterhead">
    <svg class="letterhead-shapes" viewBox="0 0 706 1000" aria-hidden="true">
      <defs>
        <linearGradient id="top-accent" x1="0" y1="0" x2="1" y2="0">
          <stop offset="0" stop-color="#1f3566"/>
          <stop offset="1" stop-color="#4d8ccc"/>
        </linearGradient>
        <linearGradient id="bottom-accent" x1="0" y1="0" x2="1" y2="1">
          <stop offset="0" stop-color="#1e3260"/>
          <stop offset="1" stop-color="#3f77bb"/>
        </linearGradient>
      </defs>
      <polygon points="0,0 706,0 706,4 410,30 0,60" fill="var(--navy)"/>
      <polygon points="410,30 706,4 706,117" fill="url(#top-accent)"/>
      <polygon points="0,829 312,930 706,777 706,1000 0,1000" fill="var(--navy)"/>
      <polygon points="0,829 312,930 155,1000 0,1000" fill="url(#bottom-accent)"/>
    </svg>

    <div class="brand">
      <span class="brand-dot"></span>
      <span class="brand-name"><span class="primary">BRETTLER</span><span class="secondary">IMMOBILIEN</span></span>
    </div>

    <p class="subject">Subject Line: Lorem ipsum dolor sit amet.</p>

    <div class="letter-body">
      <p>Lorem ipsum dolor sit amet, consectetur adipiscing elit. Maecenas at dapibus diam. Vivamus fringilla nulla lorem, sit amet mollis nisi suscipit in. Donec lacus tortor, finibus eget pharetra vitae, auctor eget augue. Mauris euismod libero ac risus fermentum, sed rhoncus erat consectetur. Phasellus eget hendrerit ligula, id volutpat tellus. Praesent viverra sapien at convallis eleifend. Pellentesque ac ipsum felis. Vestibulum augue massa, blandit eu tellus eu, fringilla volutpat quam.</p>
      <p>Nulla in neque sit amet diam lobortis lacinia. Donec tristique tristique ex in fermentum. Donec tristique erat non turpis sollicitudin, et posuere dui congue. Nulla elementum finibus orci, in varius ligula feugiat ut. Donec viverra hendrerit est, quis pulvinar metus pretium et. Lorem ipsum dolor sit amet, consectetur adipiscing elit. Nulla tempus pretium convallis. Nunc imperdiet tempus sem sit amet rutrum. Morbi tempus in lacus sed sollicitudin. Praesent non sem commodo, faucibus metus id, imperdiet odio. Morbi sodales convallis nulla a rutrum. Class aptent taciti sociosqu ad litora torquent per conubia nostra, per inceptos himenaeos. Nulla condimentum iaculis tellus non scelerisque. Fusce lobortis gravida pretium.</p>
      <p>Cras nec quam mauris. Nulla eu urna eu tortor bibendum eleifend. Nulla imperdiet semper ex, ac iaculis massa consequat eget. Maecenas quis dui varius, tincidunt massa vitae, condimentum lacus. Aliquam in viverra lorem. Integer eros tortor, tristique ac quam in, tempor accumsan lectus. Nulla in neque tellus.</p>
    </div>

    <div class="signature-mark" role="img" aria-label="Handwritten signature"></div>
    <p class="signature-label">Signature</p>

    <ul class="contact">
      <li>0123 Zip, ABC City, USA
        <svg viewBox="0 0 24 24"><path d="M12 2a7 7 0 0 0-7 7c0 5 7 13 7 13s7-8 7-13a7 7 0 0 0-7-7zm0 9.5A2.5 2.5 0 1 1 12 6.5a2.5 2.5 0 0 1 0 5z"/></svg></li>
      <li>+00 1234 56 789
        <svg viewBox="0 0 24 24"><path d="M6.6 10.8a15 15 0 0 0 6.6 6.6l2.2-2.2a1 1 0 0 1 1-.25 11.4 11.4 0 0 0 3.6.57 1 1 0 0 1 1 1V20a1 1 0 0 1-1 1A17 17 0 0 1 3 4a1 1 0 0 1 1-1h3.5a1 1 0 0 1 1 1 11.4 11.4 0 0 0 .57 3.6 1 1 0 0 1-.25 1z"/></svg></li>
      <li>info@company.com
        <svg viewBox="0 0 24 24"><path d="M2 11 22 2l-6 20-4-8z"/></svg></li>
      <li>www.company.com
        <svg viewBox="0 0 24 24"><circle cx="12" cy="12" r="10"/><circle cx="12" cy="12" r="3" fill="#1d2d52"/></svg></li>
    </ul>
  </article>

  <div class="brand standalone-brand">
    <span class="brand-dot"></span>
    <span class="brand-name"><span class="primary">BRETTLER</span><span class="secondary">IMMOBILIEN</span></span>
  </div>
</body>
</html>
```